都内でエステサロンを運営されている
美容家さんの電子書籍を出版しますので、
表紙デザイン作成をお願いいたします。

ーーーーーーーーーーー
■本のタイトル
月灯集

【サブタイトル】
朝の散歩で心を整える本

<著者>沙耶(さや)

ーーーーーーーーーー

納品は、2,560 x 1,600 ピクセルのJPEGと
元データをお願い致したく。

著者プロフィール
美容家、エステティシャン

サロンのイメージカラーはピンク、白ですが
表紙デザインに色のこだわりはありません。

ーーーー

■デザイン要望

優しさ,明るさ、清潔感と品格、プロフェッショナル感があるものをお願いします。

【コンセプト】
美容ジプシー、悩める女性たちに(男性も歓迎)贈りたい
優しく楽しい小さなご褒美タイムとその作法(洗顔やお肌のお手入れに関するメソッド)を提供する

肌質はみんなそれぞれちがいますが、本当に幸せな自分磨きは毎日のスキンケア一択。その極意を惜しみなく提供。

添付に表紙イメージの参考を挙げましたが
デザイナー様のセンスにお任せします。

ーーーーーーーーーー

※その他イラストや写真等素材を使用される場合には、商用利用可の素材をお願いします。
(Pavrelにて販売予定のため)

デザインを考えるのに必要な情報などありましたら、お答えしますので、ご遠慮なくお問い合わせ下さい。

納期は予告なく短縮する場合がございます。
よろしくお願い申し上げます。

著者様のご希望優先で決定させていただきました。

美容の道を極めた想いと、透明感、躍動感、生き生きとした理想の美人像を彷彿とさせる素敵な表紙ということで、選定させていただきます。

この度は、当コンペにご提案を頂き誠にありがとうございます。
リピートのデザイナー様もいらして、どれも素晴らしく貴重なお時間と労力を割いてくださって
本当にありがとうございました。心より感謝申し上げます。

今回選定できなかった方々の作品も大切に拝見し、個別に依頼できそうな案件などありましたらご紹介させていただきます。みなさまのご活躍祈念しております。

これからも大切に作品を制作してまいります。
どうぞまたコンペ開催の際にはご縁をいただけましたら幸いです。

本当にどうもありがとうございました。

```html
<!DOCTYPE html>
<html lang="ja">
<head>
<meta charset="utf-8">
<title>月灯集 — 朝の散歩で心を整える本</title>
<link href="https://fonts.googleapis.com/css2?family=Shippori+Mincho+B1:wght@600;800&family=Noto+Serif+JP:wght@500;700&family=Noto+Sans+JP:wght@500&display=swap" rel="stylesheet">
<style>
  :root {
    --paper: #ffffff;
    --title-pink: #e4588f;
    --ink: #3a3a3a;
    --ink-soft: #555555;
    --skin-light: #f6e7df;
    --skin: #eccfc1;
    --skin-deep: #d9ab98;
    --hair: #3a2a24;
  }
  html, body {
    margin: 0;
    padding: 0;
    overflow: hidden;
    background: var(--paper);
  }
  .cover {
    position: relative;
    width: 750px;
    height: 1200px;
    overflow: hidden;
    background: var(--paper);
  }
  .cover-photo {
    position: absolute;
    top: 0;
    right: 0;
    width: 420px;
    height: 1200px;
    background:
      radial-gradient(ellipse 260px 200px at 95% 10%, var(--hair) 0%, rgba(58,42,36,0.6) 45%, rgba(58,42,36,0) 100%),
      radial-gradient(ellipse 300px 420px at 60% 55%, var(--skin) 0%, var(--skin-light) 55%, rgba(246,231,223,0) 100%),
      radial-gradient(ellipse 260px 300px at 70% 95%, var(--skin-deep) 0%, rgba(217,171,152,0) 100%),
      var(--paper);
  }
  .cover-photo::after {
    content: "";
    position: absolute;
    inset: 0;
    background: linear-gradient(to right, var(--paper) 0%, rgba(255,255,255,0.85) 18%, rgba(255,255,255,0) 50%);
  }
  .subtitle {
    position: absolute;
    top: 42px;
    left: 38px;
    margin: 0;
    writing-mode: vertical-rl;
    font-family: "Noto Serif JP", serif;
    font-weight: 500;
    font-size: 50px;
    letter-spacing: 0.09em;
    color: var(--ink);
  }
  .title {
    position: absolute;
    top: 60px;
    left: 232px;
    margin: 0;
    writing-mode: vertical-rl;
    font-family: "Shippori Mincho B1", serif;
    font-weight: 800;
    font-size: 200px;
    line-height: 1;
    letter-spacing: 0.08em;
    color: var(--title-pink);
  }
  .byline {
    position: absolute;
    left: 212px;
    top: 1018px;
    margin: 0;
    font-family: "Shippori Mincho B1", serif;
    font-weight: 800;
    font-size: 48px;
    color: var(--ink);
    white-space: nowrap;
  }
  .byline .reading {
    font-family: "Noto Serif JP", serif;
    font-weight: 500;
    font-size: 22px;
    vertical-align: middle;
    padding: 0 2px;
  }
  .author-role {
    position: absolute;
    left: 212px;
    top: 1090px;
    margin: 0;
    font-family: "Noto Sans JP", sans-serif;
    font-weight: 500;
    font-size: 24px;
    letter-spacing: 0.02em;
    color: var(--ink-soft);
  }
</style>
</head>
<body>
  <main class="cover">
    <div class="cover-photo" role="img" aria-label="目を閉じて頬に両手を添え微笑む女性のポートレート写真"></div>
    <p class="subtitle">朝の散歩で心を整える本</p>
    <h1 class="title">月灯集</h1>
    <p class="byline">沙耶<span class="reading">(さや)</span>著</p>
    <p class="author-role">美容家・エステティシャン</p>
  </main>
</body>
</html>
```